Dental specialist needs a sharp looking letterhead

I am looking for a letterhead to be used to send letters and communication between myself (a dental specialist) and other dentists.
My office is a state of the art dental specialty office.
I need to letterhead to also state:
Gideon R. Whitfield DDS
2847 Birchmont Avenue, Suite K
West Harlow, NY 14391
(716)482-9163
fax: (716)482-9170
whitfieldroot.com (**this email address may change)

i included my logo designs.
thank you

Target Market(s)

dentists

Industry/Entity Type

Communication

Requirements
Must have
• the included logo, whether the vertical or horizontal versions

```html
<!DOCTYPE html>
<html lang="en">
<head>
<meta charset="utf-8">
<title>Birchmont Endodontics – Letterhead</title>
<link href="https://fonts.googleapis.com/css2?family=Roboto+Slab:wght@300;400;600&display=swap" rel="stylesheet">
<style>
  :root {
    --ink: #2b2b2b;
    --ink-soft: #3a3a3a;
    --brand-blue: #44a3db;
    --brand-green: #8cc63f;
    --paper: #ffffff;
    --rule: #555555;
  }
  html, body {
    margin: 0;
    padding: 0;
    width: 931px;
    height: 1200px;
    overflow: hidden;
    background: var(--paper);
  }
  .letterhead {
    position: relative;
    width: 931px;
    height: 1200px;
    background: var(--paper);
    font-family: "Roboto Slab", Georgia, serif;
    color: var(--ink);
  }
  .brand {
    position: absolute;
    left: 32px;
    top: 122px;
    display: flex;
    align-items: center;
    gap: 8px;
  }
  .brand-dot {
    width: 14px;
    height: 14px;
    border-radius: 50%;
    background: var(--brand-blue);
    flex: none;
  }
  .brand-name {
    font-weight: 600;
    font-size: 15px;
    line-height: 1.15;
    color: var(--ink);
  }
  .contact {
    position: absolute;
    left: 662px;
    top: 48px;
    height: 95px;
    border-left: 1px solid var(--rule);
    padding-left: 11px;
  }
  .contact-name {
    margin: 0;
    font-weight: 300;
    font-size: 20.5px;
    line-height: 1;
    padding-top: 2px;
    color: var(--ink-soft);
    white-space: nowrap;
  }
  .contact-list {
    list-style: none;
    margin: 10px 0 0;
    padding: 0;
  }
  .contact-item {
    display: flex;
    align-items: center;
    gap: 4px;
    font-weight: 300;
    font-size: 15px;
    line-height: 21px;
    color: var(--ink-soft);
    white-space: nowrap;
  }
  .contact-icon { width: 15px; height: 15px; flex: none; }
  .footer-band {
    position: absolute;
    left: 0;
    bottom: 0;
    width: 931px;
    height: 110px;
    background: linear-gradient(to bottom, var(--brand-green) 0%, var(--brand-blue) 45%, var(--brand-blue) 100%);
  }
  .address {
    position: absolute;
    left: 0;
    width: 931px;
    top: 1166px;
    display: flex;
    justify-content: center;
    align-items: center;
    gap: 9px;
    font-weight: 400;
    font-size: 18.5px;
    color: #ffffff;
    white-space: nowrap;
  }
  .address-pin { width: 13px; height: 18px; }
</style>
</head>
<body>
<div class="letterhead">

  <div class="brand">
    <span class="brand-dot"></span>
    <span class="brand-name">Birchmont<br>Endodontics P.C.</span>
  </div>

  <div class="contact">
    <p class="contact-name">Gideon R. Whitfield, DDS</p>
    <ul class="contact-list">
      <li class="contact-item">
        <svg class="contact-icon" viewBox="0 0 16 16" aria-hidden="true">
          <circle cx="8" cy="8" r="7" fill="none" stroke="var(--brand-blue)" stroke-width="1.3"/>
          <path d="M6 4.3c-.9.6-1.3 1.6-1 2.8.4 1.8 1.7 3.6 3.3 4.4 1 .5 2 .3 2.6-.4l-1.2-1.3c-.4.2-.8.2-1.1 0-.8-.6-1.4-1.5-1.7-2.4-.1-.4 0-.7.3-1z" fill="var(--brand-blue)"/>
        </svg>
        716-482-9163
      </li>
      <li class="contact-item">
        <svg class="contact-icon" viewBox="0 0 16 16" aria-hidden="true">
          <rect x="4" y="2" width="8" height="4" fill="var(--brand-green)"/>
          <rect x="1" y="6" width="14" height="6" rx="1.5" fill="var(--brand-green)"/>
          <rect x="4" y="10" width="8" height="4" fill="var(--brand-green)" stroke="#fff" stroke-width="1"/>
        </svg>
        716-482-9170
      </li>
      <li class="contact-item">
        <svg class="contact-icon" viewBox="0 0 16 16" aria-hidden="true">
          <rect x="1" y="3.5" width="14" height="9.5" fill="var(--brand-blue)"/>
          <path d="M1 3.5l7 5.5 7-5.5" fill="none" stroke="#fff" stroke-width="1.2"/>
        </svg>
        whitfieldroot@mailbox.com
      </li>
    </ul>
  </div>

  <div class="footer-band" role="img" aria-label="Decorative green and blue footer band"></div>

  <div class="address">
    <svg class="address-pin" viewBox="0 0 13 18" aria-hidden="true">
      <path d="M6.5 0C2.9 0 0 2.8 0 6.3 0 11 6.5 18 6.5 18S13 11 13 6.3C13 2.8 10.1 0 6.5 0z" fill="#fff"/>
      <circle cx="6.5" cy="6.3" r="2.3" fill="var(--brand-blue)"/>
    </svg>
    2847 Birchmont Avenue, Suite K, West Harlow, NY 14391
  </div>

</div>
</body>
</html>
```